Tarn Vine Collective needs a new business card design

Colour theme: Gold + Red preferred
Front side: Main logo with my details as below;
Back side: Theme of some wine glasses or bottles, maybe different color of log together
Tarn Vine Collective

Leo Park
박 성민 (this is Korean character) on the English typying board: qkr tjdals
Managing Director

Suite 7/5 Harlow Rd
South Perth WA 6151
Tel) +61(8) 6272 3058
Mob) +61(402) 617 239

leo.park@tarnvinecollective.com
tarnvine@tarnvinecollective.com
www.tarnvinecollective.com

Target Market(s)

Asian Market

Industry/Entity Type

Business

Contact Information for Business Card

Tarn Vine Collective

Leo Park
박 성민 (this is Korean character) English typying: qkr tjdals
Managing Director

Suite 7/5 Harlow Rd
South Perth WA 6151
Tel) +61(8) 6272 3058
Mob) +61(402) 617 239

Font styles to use
Serif
Decorative

Colors
ec1f27
f78f21
f04a50
faa54b
cadf82
abd036

Requirements
Must have
• Company Logo & wine theme
Nice to have
• Very simple & modern
Should not have
• No Red Color on the name of Leo Park or 박 성민
• No traditional looking. young and modern look preferred

```html
<!DOCTYPE html>
<html lang="en">
<head>
<meta charset="utf-8">
<title>Tarn Vine Collective — Business Card</title>
<link rel="stylesheet" href="https://fonts.googleapis.com/css2?family=Roboto:wght@400;500;700&family=Nanum+Myeongjo:wght@400&display=swap">
<style>
  :root {
    --wine-red: #b81826;
    --wine-red-deep: #a9141f;
    --strip-red: #d9353f;
    --gold: #b8893a;
    --charcoal: #3a3a3a;
    --ink: #4a4a4a;
    --paper: #f7f7f7;
    --backdrop: #e4e4e4;
    --white: #ffffff;
  }
  * { margin: 0; padding: 0; box-sizing: border-box; }
  html, body { width: 1200px; height: 960px; overflow: hidden; }
  body {
    background: var(--backdrop);
    position: relative;
    font-family: "Roboto", Arial, sans-serif;
  }

  .card {
    position: absolute;
    width: 600px;
    height: 342px;
    overflow: hidden;
  }

  /* Front */
  .card-front { left: 314px; top: 113px; background: var(--paper); }
  .card-front .brand {
    position: absolute; left: 36px; top: 44px;
    display: flex; align-items: center; gap: 12px;
  }
  .brand-dot { width: 26px; height: 26px; border-radius: 50%; background: var(--wine-red); }
  .card-front .brand-name {
    font-weight: 700; font-size: 27px; line-height: 1.1; color: var(--wine-red);
    letter-spacing: 0.5px;
  }
  .holder {
    position: absolute; right: 31px; top: 52px; text-align: right;
  }
  .holder-name {
    font-weight: 700; font-size: 19px; color: var(--charcoal); letter-spacing: 0.3px;
  }
  .holder-title {
    font-weight: 500; font-size: 15.5px; color: var(--gold); margin-top: 2px; letter-spacing: 0.3px;
  }
  .holder-korean {
    font-family: "Nanum Myeongjo", serif; font-size: 19px; color: var(--gold); margin-top: 2px;
  }
  .address {
    position: absolute; left: 37px; top: 168px; font-style: normal;
    font-size: 14px; line-height: 18px; color: var(--ink);
  }
  .contacts {
    position: absolute; left: 38px; top: 215px; list-style: none;
    font-size: 14px; line-height: 19px; color: var(--ink);
  }
  .contacts li { display: flex; align-items: center; gap: 8px; }
  .contacts svg { width: 14px; height: 14px; fill: var(--wine-red); flex: none; }
  .bottles {
    position: absolute; left: 414px; top: 237px; width: 138px; height: 96px;
    background: linear-gradient(90deg, #c9a24a 0%, #c2202c 30%, #c2202c 60%, #c9a24a 80%, #c2202c 100%);
    border-radius: 6px 6px 0 0;
    opacity: 0.9;
  }
  .front-strip {
    position: absolute; left: 0; bottom: 0; width: 100%; height: 10px;
    background: var(--strip-red);
  }

  /* Back */
  .card-back {
    left: 311px; top: 472px; height: 343px;
    background: radial-gradient(ellipse at 50% 45%, #c21d2b 0%, var(--wine-red-deep) 75%);
  }
  .card-back .brand {
    position: absolute; left: 0; right: 0; top: 134px;
    display: flex; justify-content: center; align-items: center; gap: 14px;
  }
  .card-back .brand-dot { background: var(--white); width: 30px; height: 30px; }
  .card-back .brand-name {
    font-weight: 700; font-size: 34px; color: var(--white); letter-spacing: 0.5px;
  }
  .back-url {
    position: absolute; left: 0; right: 0; top: 289px; text-align: center;
    font-size: 14px; color: var(--white); letter-spacing: 4.3px;
  }
</style>
</head>
<body>
  <section class="card card-front">
    <div class="brand">
      <span class="brand-dot"></span>
      <span class="brand-name">TARN VINE<br>COLLECTIVE</span>
    </div>

    <div class="holder">
      <div class="holder-name">LEO PARK</div>
      <div class="holder-title">MANAGING DIRECTOR</div>
      <div class="holder-korean">박 성민</div>
    </div>

    <address class="address">
      Suite 7/5 Harlow Rd<br>South Perth WA 6151
    </address>

    <ul class="contacts">
      <li><svg viewBox="0 0 24 24"><path d="M6.6 10.8a15.1 15.1 0 0 0 6.6 6.6l2.2-2.2a1 1 0 0 1 1-.25 11.4 11.4 0 0 0 3.6.57 1 1 0 0 1 1 1V20a1 1 0 0 1-1 1A17 17 0 0 1 3 4a1 1 0 0 1 1-1h3.5a1 1 0 0 1 1 1c0 1.25.2 2.45.57 3.6a1 1 0 0 1-.25 1z"/></svg>+61(8) 6272 3058</li>
      <li><svg viewBox="0 0 24 24"><path d="M7 1h10a2 2 0 0 1 2 2v18a2 2 0 0 1-2 2H7a2 2 0 0 1-2-2V3a2 2 0 0 1 2-2zm0 3v14h10V4zm5 15.5a1 1 0 1 0 0 2 1 1 0 0 0 0-2z"/></svg>+61(402) 617 239</li>
      <li><svg viewBox="0 0 24 24"><path d="M2 5h20v14H2zm2 2v.5l8 5 8-5V7zm0 2.8V17h16V9.8l-8 5z"/></svg>leo.park@tarnvinecollective.com</li>
      <li><svg viewBox="0 0 24 24"><path d="M2 5h20v14H2zm2 2v.5l8 5 8-5V7zm0 2.8V17h16V9.8l-8 5z"/></svg>tarnvine@tarnvinecollective.com</li>
      <li><svg viewBox="0 0 24 24"><path d="M12 2a10 10 0 1 0 0 20 10 10 0 0 0 0-20zm0 2a8 8 0 0 1 7.4 5H15V6.5A8 8 0 0 0 12 4zm-8 8a8 8 0 0 1 .3-2H8v4H4.3A8 8 0 0 1 4 12zm6 2v-4h4v4zm2 6a8 8 0 0 1-6.9-4H10v3.6a8 8 0 0 0 2 .4z"/></svg>www.tarnvinecollective.com</li>
    </ul>

    <div class="bottles" role="img" aria-label="Illustration of red and gold wine bottles and glasses"></div>
    <div class="front-strip"></div>
  </section>

  <section class="card card-back">
    <div class="brand">
      <span class="brand-dot"></span>
      <span class="brand-name">TARN VINE COLLECTIVE</span>
    </div>
    <div class="back-url">www.tarnvinecollective.com</div>
  </section>
</body>
</html>
```